Patient Satisfaction

We are extending our social listening and intelligence platform for Physicians to patient satisfaction app. Our platform monitors social media and review sites and collects, classifies and distilled patient satisfaction into nine Categories - Thoroughness, Answers Q's, Collaborative, Caring, Time Spent, Previous Success, Instruction Clarity, Follow-up and Reputation

The app will have three main states: (1) Home state showing the metric for each category, (2) a detailed page for each Category showing the metric, topics discussed and sites sourced, (3) Leaderboard showing Physicians with best scores.

If you follow our wireframes, please take liberty to extend it. We like the Lumora 6 tiles, but our wireframes fall far short of meeting its coolness and usefulness. For example, we don't have different size tiles, and would live them, or content on the tiles to make them more meaningful. [Note: use KT instead of QRM.]
Updates

The designs submitted to date look great, but they reminded me that my instructions were unclear. Feel free to follow the wireframes if you like the UI, but we also welcome your thoughts on UI in addition to look and feel. If you follow our wireframes, please take liberty to extend it. We like the Lumora 6 tile, but our wireframes falls far short of meeting its coolness and usefulness. For example, we don't have different size tiles or content on the tiles to make them more meaningful. If you've submitted designs, please feel free to revise them or submit a different look. And if you haven't submitted designs, please feel free to give us your best thoughts on UI and design.

Target Market(s)

US Physicians

Industry/Entity Type

Media

Font styles to use
Sans Serif

Colors
f37022
5c5c5c
33a6d7

Requirements
Must have
• Home state
Visual icons
Nice to have
• Leaderbaord

```html
<!DOCTYPE html>
<html lang="en">
<head>
<meta charset="utf-8">
<title>Dashboard</title>
<link rel="stylesheet" href="https://fonts.googleapis.com/css2?family=Inter:wght@300;400;500&display=swap">
<style>
  :root {
    --page-bg: #39a5d8;
    --orange: #f37022;
    --orange-light: #f6894a;
    --orange-deep: #e0621a;
    --orange-band: #ec6a1f;
    --tile-gap: #1b5f8d;
    --tile-blue: #3aa4d9;
    --tile-mid: #2e97cb;
    --tile-dark: #2688bd;
    --tile-deep: #2283b8;
    --white: #ffffff;
    --white-soft: rgba(255,255,255,0.72);
  }
  * { box-sizing: border-box; margin: 0; padding: 0; }
  html, body { width: 1024px; height: 1200px; overflow: hidden; }
  body {
    background: var(--page-bg);
    font-family: "Inter", sans-serif;
    color: var(--white);
    position: relative;
  }
  .app-screen {
    position: absolute;
    left: 192px; top: 32px;
    width: 640px; height: 1136px;
    background: var(--tile-gap);
    overflow: hidden;
  }
  .status-bar {
    position: absolute; left: 0; top: 0; width: 640px; height: 40px;
    background: var(--orange);
    display: flex; align-items: center; justify-content: space-between;
    padding: 0 14px; font-size: 22px; font-weight: 400;
  }
  .status-left, .status-right { display: flex; align-items: center; gap: 8px; width: 200px; }
  .status-right { justify-content: flex-end; }
  .status-time { font-weight: 500; }
  .signal { letter-spacing: -3px; font-size: 16px; }
  .nav-bar {
    position: absolute; left: 0; top: 40px; width: 640px; height: 88px;
    background: var(--orange);
    display: flex; align-items: center; justify-content: center;
  }
  .nav-title { font-size: 38px; font-weight: 300; }
  .nav-menu { position: absolute; left: 0; top: 34px; }
  .nav-share { position: absolute; right: 22px; top: 20px; }
  .hero {
    position: absolute; left: 0; top: 128px; width: 640px; height: 409px;
    background: linear-gradient(120deg, #f27a33 0%, #f58c4c 45%, #f9b688 75%, #f79a5e 100%);
  }
  .score-circle {
    position: absolute; left: 158px; top: 41px; width: 320px; height: 320px;
    border-radius: 50%;
    background: radial-gradient(circle at 40% 35%, #e8691f 0%, #dd5f15 60%, #d95a12 100%);
    display: flex; flex-direction: column; align-items: center; justify-content: center;
  }
  .score-value { font-size: 190px; font-weight: 300; line-height: 1; letter-spacing: -6px; margin-top: 10px; }
  .score-label { font-size: 38px; font-weight: 300; color: var(--white-soft); margin-top: -6px; }
  .stats-band {
    position: absolute; left: 0; top: 537px; width: 640px; height: 102px;
    background: var(--orange-band); display: flex;
  }
  .stat { width: 320px; position: relative; display: flex; align-items: center; }
  .stat + .stat { border-left: 1px solid rgba(0,0,0,0.08); }
  .stat-icon { margin-left: 24px; }
  .stat-text { margin-left: 12px; }
  .stat-value { font-size: 40px; font-weight: 300; line-height: 1; }
  .stat-label { font-size: 22px; font-weight: 300; color: var(--white-soft); margin-top: 4px; }
  .tile {
    position: absolute;
    display: flex; flex-direction: column; justify-content: flex-end;
    padding: 0 18px 14px;
    font-size: 23px; font-weight: 400;
  }
  .tile svg { position: absolute; }
  .tile-bedside { left: 12px; top: 653px; width: 149px; height: 140px; background: var(--tile-blue); }
  .tile-outcome { left: 174px; top: 653px; width: 148px; height: 140px; background: var(--tile-dark); }
  .tile-communication { left: 337px; top: 653px; width: 287px; height: 292px; background: var(--tile-blue); }
  .tile-knowledge { left: 11px; top: 805px; width: 311px; height: 312px; background: var(--tile-mid); }
  .tile-time { left: 337px; top: 958px; width: 287px; height: 159px; background: var(--tile-deep); }
</style>
</head>
<body>
<main class="app-screen">
  <div class="status-bar">
    <div class="status-left"><span class="signal">●●●●●</span><span>Carrio</span>
      <svg width="22" height="16" viewBox="0 0 22 16" fill="none" stroke="#fff" stroke-width="2.4" stroke-linecap="round"><path d="M2 6a13 13 0 0 1 18 0"/><path d="M5.5 9.5a8 8 0 0 1 11 0"/><circle cx="11" cy="13.5" r="1.4" fill="#fff" stroke="none"/></svg>
    </div>
    <div class="status-time">9:23 AM</div>
    <div class="status-right">
      <svg width="16" height="16" viewBox="0 0 16 16"><path d="M15 1 1 7.5l6.5 1L8.5 15z" fill="#fff"/></svg>
      <span>66%</span>
      <svg width="40" height="18" viewBox="0 0 40 18"><rect x="1" y="1" width="34" height="16" rx="2" fill="none" stroke="#fff" stroke-width="1.5"/><rect x="3" y="3" width="20" height="12" fill="#fff"/><rect x="36" y="6" width="3" height="6" fill="#fff"/></svg>
    </div>
  </div>

  <header class="nav-bar">
    <svg class="nav-menu" width="34" height="20" viewBox="0 0 34 20" stroke="#fff" stroke-width="2.5"><path d="M0 3h34M0 10h34M0 17h34"/></svg>
    <h1 class="nav-title">Dashboard</h1>
    <svg class="nav-share" width="40" height="50" viewBox="0 0 40 50" fill="none" stroke="#fff" stroke-width="2"><path d="M13 16H2v32h36V16H27"/><path d="M20 2v30M12 10l8-8 8 8"/></svg>
  </header>

  <section class="hero" role="img" aria-label="Orange grid backdrop with soft medical cross shapes">
    <div class="score-circle">
      <div class="score-value">72</div>
      <div class="score-label">KT</div>
    </div>
  </section>

  <section class="stats-band">
    <div class="stat">
      <svg class="stat-icon" width="60" height="60" viewBox="0 0 60 60" fill="none" stroke="rgba(255,255,255,0.55)" stroke-width="2"><path d="M2 4h40v26H20l-8 8v-8H2z"/><path d="M18 18h40v26H48v10l-10-10H18z" fill="var(--orange-band)"/></svg>
      <div class="stat-text"><div class="stat-value">22</div><div class="stat-label">Comments</div></div>
    </div>
    <div class="stat">
      <svg class="stat-icon" style="margin-left:30px" width="52" height="62" viewBox="0 0 52 62" fill="none" stroke="rgba(255,255,255,0.55)" stroke-width="2"><path d="M3 2v58"/><path d="M3 4c10-4 18 4 28 0s16-2 18 0v24c-6-3-12-2-18 1s-18-3-28 0"/></svg>
      <div class="stat-text"><div class="stat-value">5/15</div><div class="stat-label">Rank</div></div>
    </div>
  </section>

  <a class="tile tile-bedside">
    <svg style="left:40px;top:22px" width="66" height="60" viewBox="0 0 66 60" fill="none" stroke="#fff" stroke-width="2.4" stroke-linejoin="round"><path d="M28 4h8v6h6v8h-6v6h-8v-6h-6v-8h6z"/><path d="M4 22v36M62 36v22M4 50h58M4 40h58v-6"/><ellipse cx="30" cy="31" rx="7" ry="4"/></svg>
    Bedside
  </a>
  <a class="tile tile-outcome">
    <svg style="left:48px;top:24px" width="54" height="62" viewBox="0 0 54 62" fill="none" stroke="#fff" stroke-width="2.4"><rect x="3" y="2" width="38" height="56" rx="3"/><path d="M41 8h8v12h-8M41 24h8v12h-8M41 40h8v12h-8M11 12h22M11 19h22"/><path d="M19 28h6v6h6v6h-6v6h-6v-6h-6v-6h6z"/></svg>
    Outcome
  </a>
  <a class="tile tile-communication">
    <svg style="left:118px;top:114px" width="60" height="62" viewBox="0 0 60 62" fill="none" stroke="#fff" stroke-width="2.4"><circle cx="20" cy="30" r="8"/><path d="M5 60v-8c0-8 6-13 15-13s15 5 15 13v8z"/><path d="M44 3c8 0 14 4 14 10s-6 10-14 10l-6 5v-6c-5-2-8-5-8-9 0-6 6-10 14-10z"/></svg>
    Communication
  </a>
  <a class="tile tile-knowledge">
    <svg style="left:122px;top:120px" width="80" height="60" viewBox="0 0 80 60" fill="none" stroke="#fff" stroke-width="2.4" stroke-linejoin="round"><path d="M2 18 38 4l36 14-36 14z"/><path d="M16 24v16c0 6 10 10 22 10s22-4 22-10V24"/><path d="M74 18v22"/><circle cx="74" cy="46" r="4"/><path d="M74 50v8"/></svg>
    Knowledge
  </a>
  <a class="tile tile-time">
    <svg style="left:118px;top:30px" width="66" height="66" viewBox="0 0 66 66" fill="none" stroke="#fff" stroke-width="2.4"><circle cx="33" cy="33" r="30"/><circle cx="33" cy="33" r="24"/><path d="M24 33l7 7 11-14" stroke-linecap="round" stroke-linejoin="round"/></svg>
    Time Spent
  </a>
</main>
</body>
</html>
```